American alt-rock band needs eye-catching album cover for new record

We need an album cover for our new cd. The band is called Amber Lantern, the music is alt-rock, an interesting mix of styles and infuences- Elements of The Vanes, K7, Dan Hollis, Walt Brice The Farrows and Carl Whitmoreland are all evident in the sound. Classic rock with atmospheric elements and sweeping melodies. The album is titled "Nothing Stays Where You Left It". We are interested in designs that focus on a single direct subject and are not too busy in nature. Visually striking, yet simple and memorable. Stark contrasts between dark and light. Album covers such as Lumen Drift's "Harbinger", Gray Orchid's "Quiet Edge of The Tide" and Opal Ferry's self titled release are along the lines of what we were hoping for. An idea we had included an image of a man looking at two doors, or two paths, something involving the imagery of decisions (a door number one or number two type concept). Also like simple designs maybe with the subject in a lower corner of the image (this doesn't have to followed if it makes more sense for the image to be centered though). Solid color backgrounds. Colors we like include black, white,deep reds/blues/purples. Not all of them need to be included, but could be (white/black, white/purple, black/red, etc) Please include the band name and album name within the design.

Target Market(s)

18-39

Colors
6b449b
ec1f27
000000
474747
fbfbfb

Requirements
Must have
• Band name and album title must be included in design
Nice to have
• Would like to see something "dream-like" but not too much outer space/sci-fi imagery. Would like to see the moon motel image that I have added used in some way.
Should not have
• no skulls or heavy metal imagery. Dark is ok, but in a more artistic way.

```html
<!DOCTYPE html>
<html lang="en">
<head>
<meta charset="utf-8">
<title>Amber Lantern – Nothing Stays Where You Left It</title>
<link rel="stylesheet" href="https://fonts.googleapis.com/css2?family=Big+Shoulders+Display:wght@600;700&display=swap">
<style>
  :root {
    --frame-black: #000000;
    --cover-white: #fbfbfb;
    --type-white: #ffffff;
    --tone-teal: #8fd3d6;
    --tone-red: #e0455a;
    --tone-purple: #7a4e9e;
  }
  html, body {
    margin: 0;
    padding: 0;
    overflow: hidden;
    background: var(--frame-black);
  }
  .canvas {
    position: relative;
    width: 1200px;
    height: 1000px;
    overflow: hidden;
    background: var(--frame-black);
  }
  .album-cover {
    position: absolute;
    left: 118px;
    top: 20px;
    width: 957px;
    height: 958px;
    background: var(--cover-white);
    overflow: hidden;
  }
  .cover-art {
    position: absolute;
    left: 238px;
    top: 90px;
    width: 484px;
    height: 790px;
    background: linear-gradient(180deg,
      var(--tone-teal) 0%,
      var(--tone-teal) 38%,
      var(--tone-red) 62%,
      var(--tone-purple) 82%,
      var(--tone-purple) 100%);
  }
  .title-block {
    position: absolute;
    left: 0;
    width: 957px;
    top: 566px;
    text-align: center;
    color: var(--type-white);
    font-family: "Big Shoulders Display", "Arial Narrow", sans-serif;
    text-transform: uppercase;
  }
  .band-name {
    margin: 0;
    font-weight: 700;
    font-size: 102px;
    line-height: 98px;
    letter-spacing: 4px;
  }
  .album-title {
    margin: 14px 0 0;
    font-weight: 600;
    font-size: 32px;
    line-height: 34px;
    letter-spacing: 2px;
  }
</style>
</head>
<body>
<div class="canvas">
  <section class="album-cover">
    <div class="cover-art" role="img"
         aria-label="Photograph: a glass jar with a screw lid holding swirling teal, red and purple smoke, black cables coiled around its base"></div>
    <div class="title-block">
      <h1 class="band-name">Amber<br>Lantern</h1>
      <p class="album-title">Nothing Stays Where You Left It</p>
    </div>
  </section>
</div>
</body>
</html>
```